Website design for dressage horse training business

Looking to develop a new website design for a dressage horse training website. We want to change from a single landing page to one with multiple pages.
You are free to use your creativity to design the main landing page. This is the only page you need to design at this point. I would encourage looking at other Dressage Training websites to get a feel for what is typically on them. A few websites are listed below although I think the design of them could be better.
Notes:
- Menu to include: Home, Services, News Room, Blog, About Us, Contact,
- FAQ section on main page
- Logo to remain the same - the logo attached is not the correct color so change to match existing color.
- Change 'Sponsors' to 'Partnerships' on main page
Here is the link to the current site:
https://lindenridgestables.com/
Example sites
https://www.crestwoodsporthorsesco.com/
https://corinnalavelledressage.com/
Target Market(s)
Older women with disposable income
Number of Pages Required
1 page
Look and feel
Each slider illustrates characteristics of the customer's brand and the style your logo design should communicate.

```html
<!DOCTYPE html>
<html lang="en">
<head>
<meta charset="utf-8">
<title>Linden Ridge – Dressage &amp; Sport Horse Training</title>
<link href="https://fonts.googleapis.com/css2?family=Oswald:wght@400;500;600;700&family=Poppins:wght@400;500;600&display=swap" rel="stylesheet">
<style>
:root{
  --tan:#c39a6b;
  --tan-dark:#a97f52;
  --tan-bar:#b08559;
  --brown:#2a1f1a;
  --brown-mid:#4a3428;
  --ink:#2b2b2b;
  --muted:#8a8a8a;
  --faint:#ededed;
  --white:#ffffff;
  --head:"Oswald",sans-serif;
  --body:"Poppins",sans-serif;
}
*{margin:0;padding:0;box-sizing:border-box}
html,body{width:1200px;height:4872px;overflow:hidden}
body{position:relative;background:var(--white);font-family:var(--body);color:var(--ink)}
.abs{position:absolute}
.ph{position:absolute}
h1,h2,h3,h4{font-family:var(--head);text-transform:uppercase;font-weight:600}

/* header */
.site-header{position:absolute;top:0;left:0;width:1200px;height:64px;z-index:5;display:flex;align-items:center;justify-content:space-between;padding:0 60px}
.logo{font-family:var(--head);font-weight:600;font-size:26px;color:var(--tan);letter-spacing:1px}
.nav{display:flex;gap:30px;list-style:none}
.nav li{font-size:11px;font-weight:500;color:var(--white);letter-spacing:.5px}
.nav li.active{color:var(--tan)}

/* hero */
.hero-photo{left:0;top:0;width:1200px;height:720px;background:linear-gradient(100deg,#3a2a20 0%,#6b4c38 45%,#8a6a52 70%,#4a3428 100%)}
.hero-text{left:90px;top:225px;color:var(--white)}
.hero-text h1{font-size:74px;font-weight:700;line-height:1;letter-spacing:1px}
.hero-text .tagline{font-family:var(--head);font-size:22px;font-weight:500;text-transform:uppercase;margin-top:14px}
.hero-text .location{font-size:14px;font-weight:500;margin-top:12px}
.btn{display:inline-block;font-size:11px;font-weight:600;text-transform:uppercase;letter-spacing:.6px;padding:10px 22px;border-radius:20px}
.btn-tan{background:var(--tan);color:var(--white)}
.btn-dark{background:var(--brown);color:var(--white)}
.hero-btn{left:100px;top:505px}
.hero-tab{left:830px;top:628px;width:370px;height:142px;background:var(--tan);display:flex;align-items:flex-end;justify-content:center;padding-bottom:18px}
.hero-tab span{font-family:var(--head);font-size:52px;font-weight:600;color:var(--white);text-transform:uppercase}

/* about */
.about-photo{left:0;top:770px;width:630px;height:680px;background:linear-gradient(160deg,#d8cbbd 0%,#b59b80 45%,#7d6350 100%)}
.about-text{left:660px;top:905px;width:460px}
.section-title{font-size:40px;color:var(--brown);position:relative}
.about-text .section-title::before{content:"";position:absolute;left:0;top:-10px;width:40px;height:3px;background:var(--tan)}
.about-text p{font-size:12px;line-height:1.75;color:var(--muted);margin:18px 0 26px}
.watermark{position:absolute;font-family:var(--head);font-weight:700;text-transform:uppercase;color:var(--faint);letter-spacing:2px}
.wm-training{left:700px;top:1340px;font-size:110px}

/* services */
.services-band{left:0;top:1450px;width:875px;height:250px;background:var(--tan)}
.services-title{left:90px;top:1500px;font-size:44px;color:var(--white)}
.service-card{top:1580px;width:392px;height:430px;background:var(--white);box-shadow:0 6px 24px rgba(0,0,0,.08)}
.service-card .photo{left:0;top:0;width:392px;height:270px}
.service-card .arrow{position:absolute;right:20px;top:250px;width:40px;height:40px;border-radius:50%;background:var(--white);box-shadow:0 2px 8px rgba(0,0,0,.15);display:flex;align-items:center;justify-content:center}
.service-card h3{position:absolute;left:24px;top:300px;font-size:18px;color:var(--brown)}
.service-card p{position:absolute;left:24px;top:332px;width:340px;font-size:11.5px;line-height:1.65;color:var(--muted)}

/* for sale */
.wm-dressage{left:300px;top:2110px;font-size:100px}
.sale-text{left:90px;top:2225px;width:500px}
.sale-text h4{font-size:26px;color:var(--brown);margin-top:6px}
.sale-text p{font-size:12px;line-height:1.75;color:var(--muted);margin-top:12px}
.sale-photo{left:760px;top:2080px;width:350px;height:480px;background:linear-gradient(160deg,#e9e4dd 0%,#8a5a3a 45%,#4d2c1c 100%)}
.dots{left:608px;top:2512px;display:grid;grid-template-columns:repeat(3,10px);gap:30px}
.dots i{width:10px;height:10px;border-radius:50%;background:var(--tan);display:block}

/* faq */
.faq-photo{left:0;top:2752px;width:540px;height:570px;background:linear-gradient(135deg,#1c1410 0%,#3a2a20 55%,#5a4231 100%)}
.faq-panel{left:540px;top:2752px;width:660px;height:500px;background:var(--tan)}
.faq-title{left:610px;top:2835px;font-size:34px;color:var(--white)}
.faq-list{left:610px;top:2915px;width:520px;list-style:none}
.faq-list li{height:40px;margin-bottom:14px;background:var(--tan-bar);color:var(--white);font-size:10.5px;font-weight:500;text-transform:uppercase;display:flex;align-items:center;justify-content:space-between;padding:0 16px}
.faq-list li b{font-weight:400;font-size:14px}

/* blog */
.center-title{position:absolute;left:0;width:1200px;text-align:center;font-size:40px;color:var(--brown)}
.blog-title{top:3430px}
.blog-card{top:3508px;width:280px;height:350px;background:var(--white);box-shadow:0 6px 22px rgba(0,0,0,.08)}
.blog-card .photo{left:0;top:0;width:280px;height:200px}
.blog-card .meta{position:absolute;left:16px;top:216px;font-size:9px;color:var(--muted)}
.blog-card h3{position:absolute;left:16px;top:236px;width:250px;font-size:13px;line-height:1.35;color:var(--brown)}
.blog-card p{position:absolute;left:16px;top:284px;width:250px;font-size:9.5px;line-height:1.5;color:var(--muted)}

/* partners */
.partner-title{top:3955px}
.partner-badge{top:4050px;width:170px;height:170px;border-radius:50%;background:var(--faint);display:flex;align-items:center;justify-content:center}
.partner-badge i{display:block;width:115px;height:60px;border-radius:50%;background:#5b2d20}
.partner-badge.alt i{width:70px;height:70px;border-radius:8px;background:#9a9a9a}
.partner-info{top:4095px;width:280px}
.partner-info h3{font-size:20px;color:var(--brown)}
.partner-info p{font-size:11px;line-height:1.6;color:var(--muted);margin-top:6px}

/* footer */
.silhouette{left:0;top:4230px;width:1200px;height:310px;background:linear-gradient(180deg,#ffffff 0%,#d9d2cc 45%,#2a1f1a 100%)}
.site-footer{left:0;top:4540px;width:1200px;height:332px;background:var(--brown);color:#cfc6bf}
.footer-logo{left:90px;top:50px}
.footer-about{left:90px;top:100px;width:300px;font-size:11px;line-height:1.7}
.footer-col{top:30px}
.footer-col h4{font-size:15px;color:var(--white);letter-spacing:.6px;margin-bottom:14px;font-weight:500}
.footer-col ul{list-style:none}
.footer-col li{font-size:11px;line-height:2.05}
.footer-col li::before{content:"› ";color:var(--tan)}
.contact-row{display:flex;align-items:center;gap:10px;font-size:11px}
.socials{display:flex;gap:10px;margin-top:16px}
.socials i{width:28px;height:28px;border-radius:50%;background:var(--tan);display:block}
.newsletter p{font-size:11px;line-height:1.6;width:210px}
.newsletter .field{margin-top:12px;width:210px;height:34px;border-radius:18px;background:var(--white);font-size:10px;color:var(--muted);display:flex;align-items:center;padding-left:16px}
.newsletter .btn{margin-top:12px}
.footer-rule{left:90px;top:270px;width:1020px;height:1px;background:#4a3b32}
.copyright{left:0;top:295px;width:1200px;text-align:center;font-size:10px;color:#a99c92}
.to-top{left:1148px;top:288px;width:30px;height:30px;border-radius:50%;background:var(--tan);display:flex;align-items:center;justify-content:center}
</style>
</head>
<body>

<header class="site-header">
  <div class="logo">LINDEN RIDGE</div>
  <ul class="nav">
    <li class="active">HOME</li><li>SERVICES</li><li>NEWS ROOM</li><li>BLOG</li><li>ABOUT US</li><li>CONTACT</li>
  </ul>
</header>

<section class="hero">
  <div class="ph hero-photo" role="img" aria-label="Rider in a dark helmet beside her dressage horse in a barn"></div>
  <div class="abs hero-text">
    <h1>Heartland's</h1>
    <div class="tagline">Premier Dressage and Sport Horse Training</div>
    <div class="location">Located outside Harlow Springs</div>
  </div>
  <span class="abs btn btn-tan hero-btn">Contact Us</span>
  <div class="abs hero-tab"><span>Dressage</span></div>
</section>

<section class="about">
  <div class="ph about-photo" role="img" aria-label="Woman in a white hat and plaid shirt with a grey horse"></div>
  <div class="watermark wm-training">Training</div>
  <div class="abs about-text">
    <h2 class="section-title">About Us</h2>
    <p>As rider and trainer, Nora Whitfield began her riding career at a young age. She went up through the ranks of Pony Club with an emphasis and focus in eventing. During college, Nora worked for a small breeder starting young horses. Nora loves starting young horses including driving and guiding them in a correct and quiet way to help them flourish. Her training focuses on gymnastic work incorporating ground work, lunging, long lining, jumping, cavaletti and regular hacking and trail riding. Nora is a gold medalist having competed through Grand Prix and remains a dedicated learner...</p>
    <span class="btn btn-dark">Read More</span>
  </div>
</section>

<section class="services">
  <div class="ph services-band"></div>
  <h2 class="abs services-title">Our Services</h2>
  <article class="abs service-card" style="left:200px">
    <div class="ph photo" role="img" aria-label="Rider on horseback on a country trail" style="background:linear-gradient(150deg,#d9c7a8,#8e6e4e)"></div>
    <span class="arrow"><svg width="14" height="14" viewBox="0 0 14 14"><path d="M2 7h10M8 3l4 4-4 4" fill="none" stroke="#2a1f1a" stroke-width="1.6"/></svg></span>
    <h3>Linden Ridge Training</h3>
    <p>Linden Ridge offers both full and half time training options with regular lessons. There is much flexibility with both rides and/or lessons weekly to suit every horse.</p>
  </article>
  <article class="abs service-card" style="left:608px">
    <div class="ph photo" role="img" aria-label="Young rider in a helmet with a dark bay horse" style="background:linear-gradient(150deg,#b8a38c,#4e3626)"></div>
    <span class="arrow"><svg width="14" height="14" viewBox="0 0 14 14"><path d="M2 7h10M8 3l4 4-4 4" fill="none" stroke="#2a1f1a" stroke-width="1.6"/></svg></span>
    <h3>Linden Ridge Lessons</h3>
    <p>Lessons are available for all ages of riders. Nora thoroughly enjoys working with accomplished riders looking to succeed in the show ring with confidence.</p>
  </article>
</section>

<section class="for-sale">
  <div class="watermark wm-dressage">Dressage</div>
  <div class="abs sale-text">
    <h2 class="section-title">For Sale</h2>
    <h4>Silverline Cadence</h4>
    <p>Dressage prospect, foaled in 2012, with imported Hanoverian lines. He is incredibly quiet and kind. He is ridden by both an amateur and a child rider. He loves to hack and is very quiet alone and with a group of horses. He has shown through first level with scores into the 70s at both training and first level. He is currently solidly schooling all of second level as well as half passes and flying changes from third level. He has 3 very easy to ride gaits and it is easy for riders to sit his trot. He is quiet and well mannered on the ground with vet, farrier and clipping. He has lovely confirmation with a striking head. He is truly a one of a kind horse who loves his work!</p>
  </div>
  <div class="ph sale-photo" role="img" aria-label="Portrait of a bay dressage horse in a bridle"></div>
  <div class="abs dots"><i></i><i></i><i></i><i></i><i></i><i></i><i></i><i></i><i></i></div>
</section>

<section class="faq">
  <div class="ph faq-photo" role="img" aria-label="Dark bay horse head in a bridle against a dark background"></div>
  <div class="ph faq-panel"></div>
  <h2 class="abs faq-title">How to Write an FAQ</h2>
  <ul class="abs faq-list">
    <li>Lorem ipsum is simply dummy text of the printing? <b>+</b></li>
    <li>It is a long established fact that a reader will be distracted? <b>+</b></li>
    <li>Many desktop publishing packages and web page editors? <b>+</b></li>
    <li>There are many variations of passages of lorem ipsum available? <b>+</b></li>
    <li>Lorem ipsum is simply dummy text of the printing? <b>+</b></li>
    <li>It is a long established fact that a reader will be distracted? <b>+</b></li>
  </ul>
</section>

<section class="blog">
  <h2 class="center-title blog-title">Latest Blog Post</h2>
  <article class="abs blog-card" style="left:160px">
    <div class="ph photo" role="img" aria-label="Rider jumping a horse in an arena" style="background:linear-gradient(150deg,#c9b49a,#6d4f3a)"></div>
    <div class="meta">By admin — January 2021</div>
    <h3>01: Some blog heading goes here with description...</h3>
    <p>Lorem ipsum dolor sit amet, consectetur adipiscing elit, sed do eiusmod.</p>
  </article>
  <article class="abs blog-card" style="left:460px">
    <div class="ph photo" role="img" aria-label="Rider leading a dark horse outdoors" style="background:linear-gradient(150deg,#a99077,#3f2c20)"></div>
    <div class="meta">By admin — January 2021</div>
    <h3>02: Some blog heading goes here with description...</h3>
    <p>Lorem ipsum dolor sit amet, consectetur adipiscing elit, sed do eiusmod.</p>
  </article>
  <article class="abs blog-card" style="left:760px">
    <div class="ph photo" role="img" aria-label="Woman standing with a brown horse" style="background:linear-gradient(150deg,#d6c8b8,#7a5a44)"></div>
    <div class="meta">By admin — January 2021</div>
    <h3>03: Some blog heading goes here with description...</h3>
    <p>Lorem ipsum dolor sit amet, consectetur adipiscing elit, sed do eiusmod.</p>
  </article>
</section>

<section class="partners">
  <h2 class="center-title partner-title">Partnerships</h2>
  <div class="abs partner-badge" style="left:112px"><i></i></div>
  <div class="abs partner-info" style="left:318px">
    <h3>Fairmead Saddlery</h3>
    <p>Fairmead builds and adjusts saddles by hand, fitting each one to both horse and rider.</p>
  </div>
  <div class="abs partner-badge alt" style="left:628px"><i></i></div>
  <div class="abs partner-info" style="left:828px">
    <h3>Harrow &amp; Pike Saddlery</h3>
    <p>Our goal is to provide the best possible fit for both horse and rider whether it is a saddle you need.</p>
  </div>
</section>

<div class="ph silhouette" role="img" aria-label="Silhouette scene of riders on horseback between bare trees"></div>

<footer class="abs site-footer">
  <div class="abs logo footer-logo">LINDEN RIDGE</div>
  <p class="abs footer-about">If you are interested in learning more about Linden Ridge and our availability for training or lessons, please contact us today!</p>
  <div class="abs footer-col" style="left:472px">
    <h4>Useful Links</h4>
    <ul><li>Home</li><li>Services</li><li>News Room</li><li>Blog</li><li>About Us</li><li>Contact</li></ul>
  </div>
  <div class="abs footer-col" style="left:672px">
    <h4>Contact Me</h4>
    <div class="contact-row">
      <svg width="14" height="14" viewBox="0 0 24 24"><path d="M6.6 10.8a15 15 0 0 0 6.6 6.6l2.2-2.2a1 1 0 0 1 1-.25 11.4 11.4 0 0 0 3.6.57 1 1 0 0 1 1 1V20a1 1 0 0 1-1 1A17 17 0 0 1 3 4a1 1 0 0 1 1-1h3.5a1 1 0 0 1 1 1c0 1.25.2 2.45.57 3.57a1 1 0 0 1-.25 1z" fill="#c39a6b"/></svg>
      <span>Phone:<br>555-014-2286</span>
    </div>
    <div class="socials"><i></i><i></i><i></i></div>
  </div>
  <div class="abs footer-col newsletter" style="left:904px">
    <h4>Newsletter</h4>
    <p>Subscribe to our newsletter</p>
    <div class="field">Email Address</div>
    <span class="btn btn-tan">Subscribe</span>
  </div>
  <div class="abs footer-rule"></div>
  <div class="abs copyright">© 2021 LINDEN RIDGE. ALL RIGHTS RESERVED.</div>
  <div class="abs to-top"><svg width="12" height="12" viewBox="0 0 12 12"><path d="M2 8l4-4 4 4" fill="none" stroke="#fff" stroke-width="1.6"/></svg></div>
</footer>

</body>
</html>
```